依頼詳細
サイト構成・基本的な要件については
https://zenpiru.com/boards/kqTdnVxaPLmH52ze
を併せてご覧いただければ幸いです。

また、店舗写真・ロゴについては
http://nubalocker.jp/fetch/7b2e9d4a1c08f36e5d7a2b9c4e1f0a6d8c3b5e72
よりダウンロードいただければと存じます。

上記だけで制作が難しい場合は
http://mowlu.jp/
http://jp.gravenu.com/
http://www.lumivault.com/ja/cat-27-Beauty-Fashion.html
などから、10000円程度までならこちらにて購入可能です。
カンプデータにて作成頂き、
納品時に当方にて購入したデータに差し替えていただければと存じます。

ページ構成もシンプルですので
TOPページからすべての導線を配置するかたちでデザインいただければと存じます。
当方、jqueryなどのコーディングも対応可能ですので、
そういったデザイン提案を頂いても大丈夫です。

色合いは、店舗に合わせた、シンプルで明るい色合いを希望いたします。
木目、ブラウンを採用しているので、
そちらを展開した形のカラーパターンが合うかなと考えていますが、
特に絶対的な指定はありません。
サイトURL
http://beauty.kamobira.jp/slnH000583106/
ページ数
1ページ
希望イメージ
シンプル 複雑
単色 カラフル
暗い 明るい
日常 高級
遊び心 厳粛
未来的 伝統的
女性的 男性的
希望する色
茶系、店舗のイメージを展開するような色合いですと幸いです。
納品ファイル
• 高解像度JPG (.jpg)
• フォトショップ形式 (.psd)
補足説明
サイト構成・基本的な要件については
を併せてご覧いただければ幸いです。

また、写真・素材については
よりダウンロードいただければと存じます。

上記だけで制作が難しい場合は
http://mowlu.jp/
http://jp.gravenu.com/
などから、10000円程度までならこちらにて購入可能です。カンプデータにて作成頂き、納品時に当方にて購入したデータに差し替えていただければと存じます。

基本的には、大きなイメージ写真を前面に出して訴求しつつ
明るいイメージでまとめられればと思います。

【参考イメージ】
http://sumeragawa.jp/ (色合い、明るい印象)
http://www.bunaro.jp/home/studydesk/product/vomelq/(色合い、明るい印象)

余りかしこまった雰囲気にしてしまうよりは、柔らかく明るい印象にすることで、男女とも入りやすいサロンということをアピールできればと考えています。
制作につきましてご不明な点がございましたら、
お気軽にお申し付けいただければと存じます。
ご提案お待ちしております
ご質問にて、ワイヤーフレーム提示のご要望がありましたので追記いたします。

https://zenpiru.com/boards/hTrBnk3Yw9pLsd7c

上記が、当方で想定しているワイヤーですが、
あまり上記にこだわらず、ご提案頂ければ幸甚です。
ご不明な点がございましたらお気軽にお申し付けください。
http://nubalocker.jp/fetch/e5a08c2d7f91b3460ad2c8e17f59b04a26d3e8c1

念のため、素材を再アップいたします。

クライアントとの協議の結果、こちらの案を採用させていただきました。
スタイリッシュなデザインとサイト全体の見やすさ、信頼感、
文字などの読みやすさが大変気に入り、
そちらが採用の決め手となりました。

この度は多数ご提案いただきありがとうございました。
当選に至らなかったランサー様におかれましては大変心苦しいのですが、
次の機会にぜひご提案いただければ幸甚です。
引き続き何卒よろしくお願いいたします。

```html
<!DOCTYPE html>
<html lang="ja">
<head>
<meta charset="utf-8">
<title>CUT STUDIO LUMO</title>
<link rel="stylesheet" href="https://fonts.googleapis.com/css2?family=Noto+Sans+JP:wght@400;500;700&family=Noto+Serif+JP:wght@400;600&family=Cormorant+Garamond:wght@500;600&display=swap">
<style>
:root{
  --cream:#f7f2e8;
  --paper:#ffffff;
  --brown:#6b4a33;
  --brown-dark:#4e3423;
  --brown-soft:#a5846a;
  --beige:#ece2d0;
  --line:#d9cbb5;
  --green:#7ba23f;
  --green-dark:#5f8530;
  --orange:#d98b3a;
  --text:#5a4a3c;
}
*{box-sizing:border-box;margin:0;padding:0}
html,body{width:897px;height:1200px;overflow:hidden}
body{background:var(--cream);font-family:"Noto Sans JP",sans-serif;color:var(--text);font-size:11px;position:relative}
.topbar{height:16px;background:var(--brown);color:#e9dcc6;font-size:8px;display:flex;justify-content:space-between;align-items:center;padding:0 18px}
.header{height:56px;background:var(--beige);border-bottom:1px solid var(--line)}
.nav{display:flex;justify-content:center;height:100%}
.nav a{width:100px;display:flex;flex-direction:column;align-items:center;justify-content:center;text-decoration:none;border-right:1px solid var(--line);color:var(--brown)}
.nav a:first-child{border-left:1px solid var(--line)}
.nav .en{font-family:"Cormorant Garamond",serif;font-size:15px;font-weight:600}
.nav .ja{font-size:8px;color:var(--brown-soft)}
.hero{position:absolute;left:12px;top:78px;width:873px;height:312px;display:grid;grid-template-columns:repeat(6,1fr);grid-template-rows:1fr 1fr;gap:3px}
.photo{background:linear-gradient(135deg,#d8c7ad,#a98a6a)}
.photo.light{background:linear-gradient(135deg,#efe6d8,#c9b596)}
.photo.dark{background:linear-gradient(135deg,#8a6b52,#4f3a2b)}
.photo.warm{background:linear-gradient(135deg,#e6c9a3,#b98a5c)}
.shop-name-box{background:var(--paper);display:flex;align-items:center;justify-content:center;gap:7px}
.shop-name-box .mark{width:9px;height:9px;background:var(--brown)}
.shop-name-box .name{font-size:13px;font-weight:500;color:var(--brown);letter-spacing:1px;white-space:nowrap}
.reserve-box{background:var(--paper);display:flex;flex-direction:column;align-items:center;justify-content:center;gap:6px}
.reserve-box .label{font-size:10px;color:var(--brown-soft)}
.reserve-box .tel{font-size:18px;font-weight:700;color:var(--brown)}
.btn{display:inline-block;background:var(--orange);color:#fff;font-size:10px;padding:5px 18px;border-radius:3px}
.quote-box{background:var(--paper);display:flex;align-items:center;justify-content:center;font-family:"Noto Serif JP",serif;color:var(--brown);font-size:11px;line-height:1.9;padding:10px}
.divider{position:absolute;left:0;top:404px;width:897px;height:6px;background:linear-gradient(var(--line),transparent)}
.card{background:var(--paper);box-shadow:0 1px 4px rgba(80,50,20,.18)}
.reserve-card{position:absolute;left:135px;top:440px;width:180px;height:190px;padding:16px 14px}
.reserve-card h3{font-size:12px;color:var(--green-dark);border-bottom:2px solid var(--green);padding-bottom:5px;margin-bottom:8px}
.reserve-card .tel{font-size:18px;font-weight:700;color:var(--green-dark);margin-bottom:6px}
.reserve-card dl{font-size:9px;line-height:1.8;color:var(--text)}
.reserve-card .btn{background:var(--green);margin-top:10px;width:100%;text-align:center}
.welcome{position:absolute;left:345px;top:448px;width:420px}
.welcome h2{font-size:14px;font-weight:500;color:var(--brown);border-bottom:1px solid var(--line);padding-bottom:8px;margin-bottom:12px}
.welcome p{font-size:9.5px;line-height:2;color:var(--text)}
.recruit{position:absolute;left:135px;top:668px;width:180px}
.recruit .photo{height:110px}
.recruit .caption{text-align:center;padding:8px 0;color:var(--brown)}
.recruit .caption .en{font-family:"Cormorant Garamond",serif;font-size:18px;font-weight:600;display:block}
.recruit .caption .ja{font-size:9px}
.news{position:absolute;left:345px;top:672px;width:420px}
.news-head{display:flex;align-items:flex-end;border-bottom:2px solid var(--brown);height:22px}
.news-head .tab{background:var(--brown);color:#fff;font-family:"Cormorant Garamond",serif;font-size:13px;padding:2px 18px}
.news-head .more{margin-left:auto;font-size:8px;color:var(--brown-soft);padding-bottom:3px}
.news ul{list-style:none}
.news li{display:flex;gap:20px;font-size:9.5px;padding:9px 6px;border-bottom:1px dotted var(--line)}
.news li .date{color:var(--orange);width:60px}
.access{position:absolute;left:135px;top:910px;width:250px}
.access h2{font-family:"Cormorant Garamond",serif;font-size:22px;font-weight:600;color:var(--brown);margin-bottom:8px}
.access p{font-size:9px;line-height:1.9}
.map{position:absolute;left:420px;top:900px;width:345px;height:135px;background:linear-gradient(135deg,#e4e1da,#cfcac0)}
.to-top{position:absolute;left:812px;top:1058px;width:30px;height:30px;border-radius:50%;background:var(--green);display:flex;align-items:center;justify-content:center}
.footer{position:absolute;left:0;top:1086px;width:897px;height:114px;background:var(--brown)}
.footer-nav{display:flex;justify-content:center;gap:34px;padding:20px 0 0;flex-wrap:wrap;width:640px;margin:0 auto;row-gap:12px}
.footer-nav a{color:#efe3cf;font-size:9px;text-decoration:none}
.copy{position:absolute;bottom:0;width:100%;height:26px;background:var(--brown-dark);color:#cdb89b;font-size:8px;text-align:center;line-height:26px}
</style>
</head>
<body>
<div class="topbar"><span>カットスタジオ 広島市の美容室 CUT STUDIO LUMO</span><span>お気軽にご来店ください</span></div>
<header class="header">
  <nav class="nav">
    <a href="#"><span class="en">Top</span><span class="ja">トップ</span></a>
    <a href="#"><span class="en">Menu</span><span class="ja">メニュー</span></a>
    <a href="#"><span class="en">Reception</span><span class="ja">ご予約について</span></a>
    <a href="#"><span class="en">Staff</span><span class="ja">スタッフ紹介</span></a>
    <a href="#"><span class="en">Price</span><span class="ja">料金案内</span></a>
    <a href="#"><span class="en">Gallery</span><span class="ja">ギャラリー</span></a>
    <a href="#"><span class="en">Reservation</span><span class="ja">ご予約</span></a>
  </nav>
</header>

<section class="hero">
  <div class="photo" role="img" aria-label="サロン店内の写真"></div>
  <div class="shop-name-box"><span class="mark"></span><span class="name">CUT STUDIO LUMO</span></div>
  <div class="photo warm" role="img" aria-label="ヘアカット中の写真"></div>
  <div class="photo light" role="img" aria-label="女性スタイリストの写真"></div>
  <div class="reserve-box"><span class="label">ご予約はこちら</span><span class="tel">082-555-0147</span><span class="btn">ご予約はこちら</span></div>
  <div class="photo" role="img" aria-label="男性スタイリストの写真"></div>
  <div class="photo warm" role="img" aria-label="笑顔の女性スタッフの写真"></div>
  <div class="photo dark" role="img" aria-label="木目の店内インテリアの写真"></div>
  <div class="photo light" role="img" aria-label="セット面と椅子の写真"></div>
  <div class="quote-box"><p>「美容院に行きたい<br>けど緊張しちゃう…」<br>そんな方にぴったりの<br>カットスタジオです</p></div>
  <div class="photo" role="img" aria-label="シャンプー中の写真"></div>
  <div class="photo light" role="img" aria-label="ヘアケア商品の写真"></div>
</section>
<div class="divider"></div>

<aside class="card reserve-card">
  <h3>ご予約について</h3>
  <p class="tel">082-555-0147</p>
  <dl>
    <dt>営業時間 9:00〜19:00</dt>
    <dt>土日祝 9:00〜18:00</dt>
    <dt>定休日 毎週火曜日</dt>
  </dl>
  <span class="btn">ご予約はこちら</span>
</aside>

<section class="welcome">
  <h2>CUT STUDIO LUMO へようこそ</h2>
  <p>木のぬくもりを感じる明るい店内で、ゆったりとした時間をお過ごしいただけます。はじめての方も気軽に入れるよう、スタッフ一同心をこめてお迎えいたします。カットからカラー、パーマまで、お客様一人ひとりの髪質やライフスタイルに合わせたスタイルをご提案します。男性の方も女性の方も、どうぞお気軽にご来店ください。皆様のご来店を心よりお待ちしております。</p>
</section>

<aside class="card recruit">
  <div class="photo light" role="img" aria-label="ハサミとコームの写真"></div>
  <div class="caption"><span class="en">Recruit</span><span class="ja">求人情報</span></div>
</aside>

<section class="news">
  <div class="news-head"><span class="tab">News</span><span class="more">一覧を見る</span></div>
  <ul>
    <li><span class="date">2015.01.23</span><span>新しいカラーメニューを追加いたしました</span></li>
    <li><span class="date">2015.01.15</span><span>年始の営業時間についてのお知らせ</span></li>
    <li><span class="date">2014.12.26</span><span>年末年始の休業日についてのお知らせ</span></li>
    <li><span class="date">2014.12.10</span><span>スタッフ紹介ページを更新しました</span></li>
    <li><span class="date">2014.11.28</span><span>ホームページをリニューアルしました</span></li>
  </ul>
</section>

<section class="access">
  <h2>Access</h2>
  <p>〒730-0000<br>広島市中区桜町2-14-6<br>桜町駅より徒歩5分<br>駐車場3台完備</p>
</section>
<div class="map" role="img" aria-label="店舗周辺の地図"></div>

<a class="to-top" href="#" aria-label="ページトップへ">
  <svg width="12" height="8" viewBox="0 0 12 8"><path d="M1 7 6 2l5 5" fill="none" stroke="#fff" stroke-width="2"/></svg>
</a>

<footer class="footer">
  <nav class="footer-nav">
    <a href="#">トップ</a><a href="#">メニュー</a><a href="#">ご予約について</a><a href="#">スタッフ紹介</a><a href="#">料金案内</a><a href="#">ギャラリー</a><a href="#">ご予約</a>
    <a href="#">アクセス</a><a href="#">求人情報</a><a href="#">お知らせ</a>
  </nav>
  <div class="copy">Copyright © CUT STUDIO LUMO All Rights Reserved.</div>
</footer>
</body>
</html>
```